Design for mobile and web app for sweepstakes.

We need the design for a mobile app (planned to be build with jquery mobile) and web app (mobile first, we will use same look and feel as mobile just with displaying more info at once).

The following pages must be included:
- Userregistration/Login (Reg via Email, Chatnook-Reg)

- List of available sweepstakes (including some icons: a video icon, a "like button" type icon, a "provide some info" type of icon) this should be on the side in wep app but in mobile app its a list. possible is also a mobile display where users can swipe back and forth through it.

- single sweepstake detailview . should present a single sweepstake and give users the opportunity to participate with a button.

user settings. (doesnt not have to include a lot of fields we will at ourself. should contain some datepicker (birthday), some on/off switch (receive newsletters) some textfield in order for us to have a feel.

We have included the following files:
- prizewell_logo_final01.png:
this is our logo which should be used and also the look and feel must fit with the logo.

- prizewell_logo_final06.png:
this is the app-icon

this is a simple mockup for a registration page. the design doesnt have to contain all fields we will do that ourselfes starting from your handover, but should represent a common registration page with some fields

this is just a mockup for a possible design. not that it does use our old logo. This again is not binding is just to get a feel for what we are looking for. A list of sweepstakes and a detailspage for the sweepstake for users to participate in it.

Target Market(s)

German speaking users, Austria, Germany, Switzerland
The app is adressing a wide crowd of users who are interested in participating in sweepstakes.

Industry/Entity Type

Build

Number of Pages Required

4 page

Font styles to use
Sans Serif

Requirements
Must have
• - jquery and jquery mobile
• - html5 (preferable bootstrap-based)
• - css3
• - description on used fonts and colors. fonts must be free to use and publicly available for anyone to use.
• - all buttons should be css

```html
<!DOCTYPE html>
<html lang="de">
<head>
<meta charset="utf-8">
<title>luckora – Login</title>
<link rel="stylesheet" href="https://fonts.googleapis.com/css2?family=Montserrat:wght@300;400;500&display=swap">
<style>
  :root {
    --brand-green: #73a533;
    --text-heading: #6e7378;
    --text-label: #5e6368;
    --text-placeholder: #c4c6c8;
    --surface: #ffffff;
    --white: #ffffff;
  }
  * { box-sizing: border-box; margin: 0; padding: 0; }
  html, body {
    width: 1200px;
    height: 1020px;
    overflow: hidden;
    background: var(--surface);
    font-family: "Montserrat", Arial, sans-serif;
  }
  .login-screen {
    position: absolute;
    left: 248px;
    top: 10px;
    width: 704px;
    height: 1000px;
  }
  .brand-tile {
    position: absolute;
    left: 460px;
    top: 14px;
    width: 222px;
    height: 240px;
    border-radius: 10px;
    background: var(--brand-green);
    display: flex;
    align-items: center;
    justify-content: center;
  }
  .brand-name {
    font-size: 42px;
    font-weight: 500;
    color: var(--white);
  }
  .login-title {
    position: absolute;
    left: 51px;
    top: 218px;
    font-size: 74px;
    font-weight: 300;
    color: var(--text-heading);
    letter-spacing: -1px;
  }
  .login-form .field {
    position: absolute;
    left: 51px;
    width: 596px;
    height: 112px;
    border: 3px solid var(--brand-green);
    border-radius: 4px;
    padding: 0 18px;
    font-family: inherit;
    font-size: 40px;
    font-weight: 300;
    color: var(--text-label);
    background: var(--white);
    outline: none;
  }
  .login-form .field::placeholder { color: var(--text-placeholder); }
  .field-email { top: 343px; }
  .field-password { top: 486px; }
  .option {
    position: absolute;
    left: 55px;
    display: flex;
    align-items: center;
    gap: 22px;
    font-size: 33px;
    color: var(--text-label);
  }
  .option-save { top: 633px; }
  .option-auto { top: 699px; }
  .checkbox {
    width: 48px;
    height: 48px;
    border: 3px solid var(--brand-green);
    border-radius: 3px;
    display: flex;
    align-items: center;
    justify-content: center;
  }
  .checkbox.is-checked::after {
    content: "";
    width: 18px;
    height: 18px;
    background: var(--brand-green);
  }
  .login-button {
    position: absolute;
    left: 55px;
    top: 799px;
    width: 288px;
    height: 116px;
    border: none;
    border-radius: 3px;
    background: var(--brand-green);
    color: var(--white);
    font-family: inherit;
    font-size: 42px;
    font-weight: 500;
    display: flex;
    align-items: center;
    justify-content: center;
    gap: 12px;
  }
  .login-button svg { width: 32px; height: 28px; }
</style>
</head>
<body>
  <main class="login-screen">
    <div class="brand-tile">
      <span class="brand-name">luckora</span>
    </div>

    <h1 class="login-title">Login</h1>

    <form class="login-form">
      <input class="field field-email" type="email" placeholder="email">
      <input class="field field-password" type="password" placeholder="password">

      <label class="option option-save">
        <span class="checkbox"></span>
        password speichern
      </label>
      <label class="option option-auto">
        <span class="checkbox is-checked"></span>
        automatischer login
      </label>

      <button class="login-button" type="button">
        Login
        <svg viewBox="0 0 32 28" aria-hidden="true">
          <polyline points="3,5 12,14 3,23" fill="none" stroke="#ffffff" stroke-width="5"/>
          <polyline points="17,5 26,14 17,23" fill="none" stroke="#ffffff" stroke-width="5"/>
        </svg>
      </button>
    </form>
  </main>
</body>
</html>
```